distributor of aftermarket auto electrical components

I am after business card design for my new company called
Summit Vehicle Supplies (SVS as the acronym). I will supplying automotive wiring components, basically from battery to headlight. I will be aiming to sell in the 4wd scene and to auto electricians. i am not worried which colours are used though i would like it to be dynamic.
Updates

sorry guys, i have add a mobile and e-mail address that will need to on there as well. Sorry for theĀ inconvenience.

sorry guys i had erred on my spelling with my e-mail. i have now fixed it in the brief

Target Market(s)

4wd industry, custom cars, RV, auto electricians

Industry/Entity Type

Electrical

Requirements
Must have
• Company Name
ABN number: 71 306 548 290
Director: Derek Holloway
M 0432 718 946
E dhollo@fernwire.com.au

```html
<!DOCTYPE html>
<html lang="en">
<head>
<meta charset="utf-8">
<title>Summit Vehicle Supplies – Business Card</title>
<link rel="stylesheet" href="https://fonts.googleapis.com/css2?family=Ubuntu:wght@700&family=Fira+Sans:wght@600&family=Noto+Serif:ital,wght@1,400;1,700&display=swap">
<style>
  :root {
    --ink: #1a1a1a;
    --accent: #f0141e;
    --paper: #ffffff;
    --rule: #111111;
  }
  html, body {
    margin: 0;
    padding: 0;
    width: 1200px;
    height: 706px;
    overflow: hidden;
    background: var(--paper);
  }
  .card {
    position: relative;
    width: 1200px;
    height: 706px;
    background: var(--paper);
  }
  .brand-mark {
    position: absolute;
    left: 0;
    top: -16px;
    width: 1200px;
    text-align: center;
    font-family: "Ubuntu", sans-serif;
    font-weight: 700;
    font-size: 420px;
    line-height: 420px;
    letter-spacing: 40px;
    text-indent: 40px;
    color: var(--ink);
    margin: 0;
  }
  .company-name {
    position: absolute;
    left: 0;
    top: 356px;
    width: 1200px;
    text-align: center;
    font-family: "Ubuntu", sans-serif;
    font-weight: 700;
    font-size: 68px;
    line-height: 76px;
    letter-spacing: 7px;
    color: var(--accent);
    margin: 0;
  }
  .divider {
    position: absolute;
    left: 0;
    top: 440px;
    width: 1200px;
    height: 7px;
    background: var(--rule);
  }
  .director {
    position: absolute;
    left: 268px;
    top: 468px;
    font-family: "Noto Serif", serif;
    font-style: italic;
    color: var(--ink);
    margin: 0;
    white-space: nowrap;
  }
  .director-label {
    font-size: 36px;
    font-weight: 400;
  }
  .director-name {
    font-size: 64px;
    font-weight: 700;
    margin-left: 10px;
  }
  .contact {
    position: absolute;
    left: 40px;
    margin: 0;
    font-family: "Fira Sans", sans-serif;
    font-weight: 600;
    font-size: 34px;
    line-height: 44px;
    color: var(--ink);
    white-space: nowrap;
  }
  .contact-mobile { top: 580px; }
  .contact-email { top: 630px; }
  .abn {
    position: absolute;
    right: 26px;
    top: 620px;
    font-family: "Fira Sans", sans-serif;
    font-weight: 600;
    font-size: 56px;
    line-height: 64px;
    color: var(--accent);
    margin: 0;
    white-space: nowrap;
  }
</style>
</head>
<body>
  <main class="card">
    <h1 class="brand-mark">SVS</h1>
    <p class="company-name">Summit Vehicle Supplies</p>
    <div class="divider"></div>
    <p class="director"><span class="director-label">director:</span><span class="director-name">Derek Holloway</span></p>
    <p class="contact contact-mobile">M 0432 718 946</p>
    <p class="contact contact-email">E dhollo@fernwire.com.au</p>
    <p class="abn">ABN: 71 306 548 290</p>
  </main>
</body>
</html>
```